Webpage design for a translation agancy

We need to update and modernize our current Wordpress webpage www.verbanova.se. I am happy with the basics but there are definitely room for an update.
We are a translation agency providing translation services B2B. We supply translations to different industries. Law, HR, Medical, Financial, IT, Technical, Business. Our clients are mostly Swedish based companies.
We would like to see designs that:
- Increases our conversions
- Conveys reliance to our visitors/clients
- Keeps the framework on our current webpage (more or less)
- The quote bottom and quotation form is a crucial for our business. Drag and drop is a must.
-We'd like to keep the banner pics. One of them is our view from our office and the two others are local pictures from Stockholm/Sweden. The banner and the quote has to be integrated in the update.
-The design has to include designs for the whole webpage, landing page and all other pages.
/Teodor
Target Market(s)
Our target market is Swedish companies, b2b, operating in different industries. Law, Finance, Medical, IT, HR, Marketing, Engineering. Only B2B. Our typical buyer is a decision maker/ middle management.
Requirements
Must have
- - Conveys reliance to our visitors/clients
- - Our current Unique Selling Points
- - Keeps the framework on our current webpage (more or less)
- - The quote bottom and quotation form is a crucial for our business. One compeditor whom has a good solution for the quote form is, www.lingmarka.lv/en/
- -We'd like to keep the banner pics. One of them is our view from our office and the two others are local pictures from Stockholm/Sweden. The banner and the quote has to be integrated in the update.
- -The design has to include designs for the whole webpage, landing page and all other pages.
Nice to have
- Pretty much same color scales as today.

```html
<!DOCTYPE html>
<html lang="en">
<head>
<meta charset="utf-8">
<title>Verbanova – Translation Agency</title>
<link href="https://fonts.googleapis.com/css2?family=Roboto:ital,wght@0,300;0,400;0,500;0,700;1,300;1,400&display=swap" rel="stylesheet">
<style>
:root{
  --purple:#9a5fd3;
  --green:#8cc63f;
  --blue:#5cb6d8;
  --teal:#4fa3c7;
  --ink:#333;
  --text:#555;
  --muted:#888;
  --grey:#ededee;
  --light:#f6f6f6;
  --dark:#5d5d5d;
}
*{box-sizing:border-box;margin:0;padding:0}
html,body{width:1200px;height:4036px;overflow:hidden;background:#fff}
body{font-family:'Roboto',sans-serif;color:var(--text);position:relative}
.sec{position:absolute;left:0;width:1200px}
.abs{position:absolute}
.rainbow{height:4px;background:linear-gradient(90deg,var(--green) 0 25%,var(--blue) 25% 50%,var(--purple) 50% 75%,#f0a830 75% 100%)}
/* utility bar */
.util{top:0;height:38px}
.util-links{position:absolute;right:40px;top:12px;display:flex;gap:18px;font-size:11px;color:var(--ink)}
.util-links span::before{content:"";display:inline-block;width:7px;height:7px;border-radius:50%;background:var(--teal);margin-right:5px;vertical-align:middle}
/* nav */
.nav{top:38px;height:92px;border-top:1px solid #eee}
.brand{position:absolute;left:161px;top:30px;font-size:30px;font-weight:500;color:var(--ink);display:flex;align-items:center;gap:8px}
.brand i{width:12px;height:12px;border-radius:50%;background:var(--blue);display:block}
.menu{position:absolute;right:160px;top:38px;display:flex;gap:36px;font-size:14px;color:var(--ink)}
/* hero */
.hero{top:130px;height:534px;background:linear-gradient(180deg,#cfd3d8 0%,#e7e8ea 45%,#b9bcc0 100%)}
.hero-band{position:absolute;left:0;top:214px;width:650px;height:108px;background:rgba(154,95,211,.88)}
.hero-band h1{position:absolute;left:180px;top:36px;font-size:26px;font-weight:500;color:#fff;letter-spacing:.5px}
.hero-arrow{position:absolute;top:250px}
.quote-btn{position:absolute;left:500px;top:638px;width:198px;height:52px;background:var(--green);color:#fff;font-size:16px;font-weight:500;display:flex;align-items:center;justify-content:center;z-index:2}
/* headings */
.h2{font-size:28px;font-weight:300;color:var(--ink)}
.p{font-size:12px;line-height:19px;color:var(--text)}
/* how it works */
.how{top:664px;height:356px;border-bottom:1px solid #e4e4e4}
.badge{position:absolute;left:885px;top:52px;display:flex;gap:10px;align-items:center;font-size:9px;color:var(--ink);width:170px}
.badge b{width:30px;height:38px;border:2px solid var(--teal);border-radius:3px;display:block}
.step{position:absolute;top:170px;width:250px}
.step h3{margin-top:18px;font-size:15px;font-weight:400;color:var(--blue)}
.step .p{margin-top:8px}
.step-arrow{position:absolute;top:200px}
/* agency */
.agency{top:1020px;height:420px;border-bottom:1px solid #e4e4e4}
.agency-art{position:absolute;left:753px;top:105px;width:320px;height:320px;border-radius:50%;background:radial-gradient(circle,#f4f4f4 0%,#dcdde0 100%)}
/* why */
.why{top:1440px;height:578px}
.feature{position:absolute;width:270px}
.feature .ic{position:absolute;left:0;top:0;width:88px;height:88px;border-radius:50%;background:#e6e9ec;display:flex;align-items:center;justify-content:center}
.feature .tx{position:absolute;left:110px;top:4px;width:170px}
.feature h4{font-size:13px;font-weight:500;color:var(--blue);letter-spacing:.5px}
.feature .p{font-size:11px;line-height:17px;margin-top:6px}
.score{position:absolute;left:835px;top:90px;width:200px;height:325px;border:2px solid var(--green);padding:20px 22px}
.score .num{font-size:44px;font-weight:700;color:var(--green)}
.score .lbl{font-size:21px;font-weight:300;color:var(--ink);line-height:28px}
.score .qt{margin-top:22px;font-size:13px;font-style:italic;line-height:22px;color:#aaa;font-weight:300}
/* industry */
.industry{top:2018px;height:562px;background:var(--grey)}
.tile{position:absolute;width:205px;height:202px;color:#fff;display:flex;flex-direction:column;align-items:center;justify-content:center;gap:14px;font-size:13px;letter-spacing:.5px}
.tile .cap{font-size:10px;line-height:14px;text-align:center;padding:0 14px;letter-spacing:0}
/* testimonials */
.testi{top:2580px;height:425px;background:var(--blue)}
.testi h2{position:absolute;left:0;width:1200px;top:160px;text-align:center;font-size:28px;font-weight:300;color:#fff}
.avatar{position:absolute;left:245px;top:212px;width:100px;height:100px;border-radius:50%;background:linear-gradient(135deg,#c79a7c,#6e5446);border:3px solid #fff}
.testi-text{position:absolute;left:385px;top:224px;width:670px;font-size:11.5px;line-height:19px;font-style:italic;color:#eaf6fb}
.testi-name{position:absolute;left:385px;top:290px;font-size:11px;font-weight:500;color:#fff}
.dots{position:absolute;left:565px;top:368px;display:flex;gap:6px}
.dots i{width:10px;height:10px;border-radius:50%;background:rgba(255,255,255,.55);display:block}
.dots i:first-child{background:#fff}
/* news */
.news{top:3005px;height:613px}
.card{position:absolute;top:115px;width:272px}
.card .img{height:248px}
.card .soc{margin-top:22px;display:flex;gap:10px}
.card .soc i{width:9px;height:9px;border-radius:50%;background:var(--teal);display:block}
.card h3{margin-top:18px;font-size:17px;font-weight:400;color:var(--ink)}
.card .p{font-size:10.5px;line-height:16px;margin-top:10px}
.card .meta{margin-top:14px;font-size:10px;color:var(--teal)}
/* clients */
.clients{top:3618px;height:108px;display:flex;justify-content:center;align-items:center;gap:46px;font-size:15px;font-weight:500;color:#8a8a8a}
.colorline{top:3726px}
/* footer */
.footer{top:3730px;height:306px;background:var(--light)}
.fcol{position:absolute;top:66px}
.fcol h5{font-size:12px;font-weight:500;color:var(--ink);letter-spacing:.5px;margin-bottom:16px}
.fcol p{font-size:11px;line-height:20px;color:var(--text)}
.fbottom{position:absolute;left:161px;right:161px;top:235px;border-top:1px solid #ddd;padding-top:18px;display:flex;justify-content:space-between;align-items:center;font-size:10px;color:var(--ink)}
.fsoc{display:flex;gap:8px}
.fsoc i{width:22px;height:22px;border-radius:50%;background:var(--teal);display:block}
</style>
</head>
<body>

<div class="sec rainbow" style="top:0"></div>
<header>
<div class="sec util">
  <div class="util-links"><span>Contact us</span><span>Request a quote</span><span>Language ▾</span><span>Interpreter</span></div>
</div>
<nav class="sec nav">
  <div class="brand"><i></i>verbanova</div>
  <div class="menu"><span>Our services</span><span>Translation methods</span><span>Customer cases</span><span>About us</span><span>Stockholm</span><span>For Translators</span></div>
</nav>
</header>

<section class="sec hero" role="img" aria-label="Banner photo: view from the office over a glass-roofed atrium in Stockholm">
  <div class="hero-band"><h1>KVALITET AR VIKTIGT FOR OSS</h1></div>
  <svg class="hero-arrow" style="left:55px" width="20" height="36" viewBox="0 0 20 36"><path d="M17 2 3 18l14 16" fill="none" stroke="#fff" stroke-width="2"/></svg>
  <svg class="hero-arrow" style="right:55px" width="20" height="36" viewBox="0 0 20 36"><path d="M3 2l14 16L3 34" fill="none" stroke="#fff" stroke-width="2"/></svg>
</section>
<div class="quote-btn">REQUEST QUOTE</div>

<section class="sec how">
  <h2 class="h2 abs" style="left:161px;top:56px">How it Works</h2>
  <div class="badge"><b></b>Svenska professionella översättare</div>

  <div class="step" style="left:161px">
    <svg width="56" height="60" viewBox="0 0 56 60"><rect x="8" y="6" width="34" height="46" rx="2" fill="none" stroke="var(--blue)" stroke-width="2"/><path d="M15 18h20M15 26h20M15 34h14" stroke="var(--blue)" stroke-width="2"/><path d="M40 44l10-20 4 2-10 20-5 3z" fill="var(--blue)"/></svg>
    <h3>1.REQUEST A QUOTE</h3>
    <p class="p">Sed ut perspiciatis unde omnis iste natus erri volu ptatem accusantium doloremque laudum.</p>
  </div>
  <svg class="step-arrow" style="left:300px" width="150" height="12" viewBox="0 0 150 12"><path d="M0 6h144M138 1l6 5-6 5" fill="none" stroke="#bbb" stroke-width="1.5"/></svg>
  <div class="step" style="left:473px">
    <svg width="56" height="60" viewBox="0 0 56 60"><circle cx="22" cy="24" r="15" fill="none" stroke="var(--blue)" stroke-width="2.5"/><path d="M33 35l16 16" stroke="var(--blue)" stroke-width="5" stroke-linecap="round"/></svg>
    <h3>2.WE ANALYZE</h3>
    <p class="p">Sed ut perspiciatis unde omnis iste natus erri volu ptatem accusantium doloremque laudum.</p>
  </div>
  <svg class="step-arrow" style="left:620px" width="150" height="12" viewBox="0 0 150 12"><path d="M0 6h144M138 1l6 5-6 5" fill="none" stroke="#bbb" stroke-width="1.5"/></svg>
  <div class="step" style="left:793px">
    <svg width="56" height="60" viewBox="0 0 56 60"><rect x="6" y="20" width="44" height="30" fill="none" stroke="var(--blue)" stroke-width="2"/><path d="M6 20l22 16 22-16M16 20V8h24v12" fill="none" stroke="var(--blue)" stroke-width="2"/></svg>
    <h3>3.YOU'LL GET A FREE QUOTE</h3>
    <p class="p">Sed ut perspiciatis unde omnis iste natus erri volu ptatem accusantium doloremque laudum.</p>
  </div>
</section>

<section class="sec agency">
  <svg class="abs" style="left:0;top:0" width="1200" height="420"><polygon points="770,0 1200,0 1200,420 690,420" fill="var(--grey)"/></svg>
  <div class="agency-art" role="img" aria-label="Line illustration of world landmarks and languages around a circle"></div>
  <h2 class="h2 abs" style="left:161px;top:82px">Verbanova Translation Agency</h2>
  <div class="abs" style="left:161px;top:140px;width:595px">
    <p class="p">Verbanova is a translation agency that provides language services of the highest quality and maintains a strong focus on you, the customer. We assist our customers on a daily basis by translating industry-specific documentation to a wide variety of languages. Our project managers ensure that you receive expert help from our highly qualified specialist translators, who will adapt your text to the relevant target audience.</p>
    <p class="p" style="margin-top:16px">Irrespective of whether your project comprises technical manuals, legal documentation, annual reports or websites, we can assist you. Our business concept is to provide translation services with a strong focus on personal service and quality.</p>
    <p class="p" style="margin-top:16px">Our goal is always to build long term partnerships with our customers.</p>
  </div>
</section>

<section class="sec why">
  <h2 class="h2 abs" style="left:161px;top:88px">Why Us?</h2>
  <p class="p abs" style="left:161px;top:140px;width:600px">Sed ut perspiciatis unde omnis iste natus error sit voluptatem accusantium doloremque laudantium, totam rem aperiam, eaque ipsa quae ab illo inventore veritatis et quasi architecto beata.</p>

  <div class="feature" style="left:161px;top:233px">
    <div class="ic"><svg width="40" height="44" viewBox="0 0 40 44"><circle cx="20" cy="16" r="12" fill="none" stroke="var(--teal)" stroke-width="3"/><path d="M12 26l-4 16 12-6 12 6-4-16" fill="var(--teal)"/></svg></div>
    <div class="tx"><h4>QUALITY</h4><p class="p">Vi fokuserar på att hålla hög kvalitet i alla våra översättningsprocesser, från projektledning, översättning...</p></div>
  </div>
  <div class="feature" style="left:455px;top:233px">
    <div class="ic"><svg width="40" height="40" viewBox="0 0 40 40"><circle cx="20" cy="20" r="16" fill="none" stroke="var(--teal)" stroke-width="3"/><path d="M20 10v11l7 5" fill="none" stroke="var(--teal)" stroke-width="3"/></svg></div>
    <div class="tx"><h4>DELIVERY</h4><p class="p">Vi har som mål att möta samtliga våra uppdrag hålla bästa möjliga leveranstid och att leverera i format som</p></div>
  </div>
  <div class="feature" style="left:161px;top:388px">
    <div class="ic"><svg width="40" height="40" viewBox="0 0 40 40"><path d="M22 4a14 14 0 0 0-14 14c0 5 2 8 4 10v8h14v-5h5l2-7 3-1-4-5c0-8-4-14-10-14z" fill="var(--teal)"/></svg></div>
    <div class="tx"><h4>COMPETENCE</h4><p class="p">Som översättningsbyrå har vi krav på oss att alltid ligga steget före. Vi jobbar enbart med branschens mest.</p></div>
  </div>
  <div class="feature" style="left:455px;top:388px">
    <div class="ic"><svg width="40" height="40" viewBox="0 0 40 40"><circle cx="14" cy="14" r="9" fill="none" stroke="var(--teal)" stroke-width="4"/><path d="M20 20l16 16M30 30l4-4M26 26l3-3" stroke="var(--teal)" stroke-width="4"/></svg></div>
    <div class="tx"><h4>SECRECY</h4><p class="p">Vi behandlar alla våra kunders uppdrag och dokument med höga krav på säkerhet och sekretess.</p></div>
  </div>

  <div class="score">
    <div class="num">98%</div>
    <div class="lbl">Customer Satisfaction.</div>
    <svg class="abs" style="left:22px;top:150px" width="20" height="16" viewBox="0 0 20 16"><path d="M0 16V9L4 0h4L5 8h3v8zM11 16V9l4-9h4l-3 8h3v8z" fill="#ddd"/></svg>
    <p class="qt" style="padding-left:26px">Sed ut persp iciatis unde omnis iste natu sit vol tat em accus antiumdoloreme lauda ntium, totam remeriam, eaxe ipsa quae.</p>
  </div>
</section>

<section class="sec industry">
  <svg class="abs" style="left:500px;top:0" width="200" height="40" viewBox="0 0 200 40"><path d="M0 0h200c-60 0-80 8-100 40C80 8 60 0 0 0z" fill="#fff"/></svg>
  <h2 class="h2 abs" style="left:161px;top:112px;line-height:38px">We know<br>your industry</h2>
  <p class="p abs" style="left:161px;top:205px;width:205px;font-size:11px;line-height:17px">Sed ut perspiciatis unde omnis iste natus error doloremque laudantium, totam rem aperiam, eaque ipsa quae ab illo inventore veritatis et quasi architecto beata.</p>

  <div class="tile" style="left:385px;top:110px;background:linear-gradient(135deg,#9ed14e,#7cb235)" role="img" aria-label="Law photo with green overlay">
    <svg width="50" height="40" viewBox="0 0 50 40"><path d="M25 2v34M12 36h26M6 8h38M6 8 0 22h12zM44 8l-6 14h12z" fill="none" stroke="#fff" stroke-width="2.5"/></svg>LAW</div>
  <div class="tile" style="left:605px;top:110px;background:linear-gradient(135deg,#5b92d8,#3f6fb8)" role="img" aria-label="HR photo with blue overlay">
    <svg width="40" height="44" viewBox="0 0 40 44"><circle cx="20" cy="11" r="9" fill="#fff"/><path d="M2 44c0-14 8-20 18-20s18 6 18 20z" fill="#fff"/></svg>HR</div>
  <div class="tile" style="left:828px;top:110px;background:linear-gradient(135deg,#b57fe0,#9a5fd3)" role="img" aria-label="Medical photo with purple overlay">
    <svg width="48" height="40" viewBox="0 0 48 40"><rect x="2" y="8" width="44" height="30" rx="3" fill="#fff"/><path d="M17 8V2h14v6" fill="none" stroke="#fff" stroke-width="3"/><path d="M24 14v18M15 23h18" stroke="#b57fe0" stroke-width="5"/></svg>MEDICAL</div>

  <div class="tile" style="left:161px;top:325px;background:linear-gradient(135deg,#6b6b6b,#4a4a4a)" role="img" aria-label="Financial photo with dark overlay">
    <svg width="36" height="40" viewBox="0 0 36 40"><path d="M12 2h12l-4 8c10 4 14 14 14 20 0 6-6 8-16 8S2 36 2 30c0-6 4-16 14-20z" fill="#fff"/></svg>FINANCIAL<span class="cap">When translating annual reports or other financial material, it is essential to use a translator with specialist</span></div>
  <div class="tile" style="left:385px;top:325px;background:linear-gradient(135deg,#b47ee0,#955ad0)" role="img" aria-label="IT photo with purple overlay">
    <svg width="48" height="40" viewBox="0 0 48 40"><rect x="4" y="4" width="40" height="26" rx="2" fill="none" stroke="#fff" stroke-width="2.5"/><path d="M0 36h48" stroke="#fff" stroke-width="3"/></svg>IT</div>
  <div class="tile" style="left:605px;top:325px;background:linear-gradient(135deg,#6cc0d8,#4fa3c7)" role="img" aria-label="Technical photo with blue overlay">
    <svg width="44" height="40" viewBox="0 0 44 40"><circle cx="16" cy="22" r="10" fill="none" stroke="#fff" stroke-width="5" stroke-dasharray="5 3"/><circle cx="33" cy="9" r="6" fill="none" stroke="#fff" stroke-width="4" stroke-dasharray="3 2"/></svg>TECHNICAL</div>
  <div class="tile" style="left:828px;top:325px;background:linear-gradient(135deg,#9ed14e,#7cb235)" role="img" aria-label="Business photo with green overlay">
    <svg width="46" height="40" viewBox="0 0 46 40"><path d="M4 38V28M14 38V22M24 38V26M34 38V16" stroke="#fff" stroke-width="5"/><path d="M2 22 16 10l8 6L42 2M34 2h8v8" fill="none" stroke="#fff" stroke-width="2.5"/></svg>BUSINESS</div>
</section>

<section class="sec testi">
  <svg class="abs" style="left:500px;top:0" width="200" height="40" viewBox="0 0 200 40"><path d="M0 0h200c-60 0-80 8-100 40C80 8 60 0 0 0z" fill="var(--grey)"/></svg>
  <h2>Our Testimonials</h2>
  <div class="avatar" role="img" aria-label="Portrait photo of a client"></div>
  <p class="testi-text">❝ Sed ut perspiciatis unde omnis iste natus error sit voluptatemaccusantium laudantium, totam rem aperiam, eaqu rem accusantium doloremque laudantium, totam rem aperiam, eaque ipsa quae ab illo inventore veritatis et quasi architecto beatae vitae dicta sunt explicabo. Nemo enim ipsam voluptatem quia voluptas sit aspernatur ❞</p>
  <div class="testi-name">Head of Fulfillment, City Name</div>
  <div class="dots"><i></i><i></i><i></i><i></i></div>
</section>

<section class="sec news">
  <h2 class="h2 abs" style="left:0;width:1200px;top:52px;text-align:center;font-size:30px">Latest News</h2>
  <p class="p abs" style="left:340px;width:520px;top:117px;text-align:center;font-size:11px;line-height:17px">Sed ut perspiciatis unde omnis iste natus error sit voluptatem accusantium doloremque laudantium, totam rem aperiam, eaque ipsa quae ab illo inventore veritatis et quasi architecto beata.</p>

  <article class="card" style="left:161px">
    <div class="img" role="img" aria-label="Photo of a finger pressing a keyboard key" style="background:linear-gradient(135deg,#f3f3f3,#d9d9d9 60%,#e58a7a)"></div>
    <div class="soc"><i></i><i></i><i></i></div>
    <h3>Framtiden för världens språk</h3>
    <p class="p">At vlenero eos et accusamus et accusamus et iusto ricocimsuptiditate non provident, similique subintio fll cia deserunt mollitia animi.</p>
    <div class="meta">▦ 20 FEB 2017 &nbsp;|&nbsp; ◯ Comments (0)</div>
  </article>
  <article class="card" style="left:463px">
    <div class="img" role="img" aria-label="Photo of a city skyline at sunset" style="background:linear-gradient(180deg,#7f8fa6 0%,#e9a95a 55%,#4a4236 100%)"></div>
    <div class="soc"><i></i><i></i><i></i></div>
    <h3>Framtiden för världens språk</h3>
    <p class="p">At vlenero eos et accusamus et accusamus et iusto ricocimsuptiditate non provident, similique subintio fll cia deserunt mollitia animi.</p>
    <div class="meta">▦ 20 FEB 2017 &nbsp;|&nbsp; ◯ Comments (0)</div>
  </article>
  <article class="card" style="left:765px">
    <div class="img" role="img" aria-label="Photo of a laptop keyboard beside a glass globe" style="background:linear-gradient(135deg,#e7eef5,#9db0c8 60%,#5f7390)"></div>
    <div class="soc"><i></i><i></i><i></i></div>
    <h3>Framtiden för världens språk</h3>
    <p class="p">At vlenero eos et accusamus et accusamus et iusto ricocimsuptiditate non provident, similique subintio fll cia deserunt mollitia animi.</p>
    <div class="meta">▦ 20 FEB 2017 &nbsp;|&nbsp; ◯ Comments (0)</div>
  </article>
</section>

<section class="sec clients" style="background:var(--light)">
  <span>Norrvik</span><span>Halden &amp; Co</span><span>Brightwater Invest</span><span>Stellan Data</span><span>Maren Travel</span><span>Vestra</span>
</section>
<div class="sec rainbow colorline"></div>

<footer class="sec footer">
  <div class="fcol" style="left:161px;top:60px;width:200px">
    <div style="font-size:26px;font-weight:500;color:var(--ink);margin-bottom:14px">verbanova</div>
    <p>Verbanova is a translation agency that provides language services of the highest quality and maintains a strong focus on you, the customer.</p>
  </div>
  <div class="fcol" style="left:410px"><h5>VERBANOVA AB</h5><p>Request a Quote<br>Contact<br>About Verbanova<br>VAT: SE559900112201</p></div>
  <div class="fcol" style="left:588px"><h5>TRANSLATION SERVICES</h5><p>Technical translations<br>Legal Translations<br>Financial translations<br>Medical translations</p></div>
  <div class="fcol" style="left:790px"><h5>ABOUT US</h5><p>News<br>About us<br>Contact us</p></div>
  <div class="fcol" style="left:925px"><h5>VERBANOVA AB</h5><p>Ringvägen 12,<br>SE-118 60, Stockholm<br>+46 (0) 8 555 01 00</p></div>
  <div class="fbottom">
    <div class="fsoc"><i></i><i></i><i></i><i></i></div>
    <div>© 2017 Verbanova. All Copyrights are Reserved.Terms of Use &nbsp;&nbsp; Privacy Policy &nbsp;&nbsp; Sitemap</div>
  </div>
</footer>

</body>
</html>
```